Modern corporate energy/fuel business need business card design

Business card required for company founder. Korvan Advanced Energy is a Australian based modern energy/fuel provider. We offer specialised solutions to businesses using fossil fuels through renewable energy solutions.

I would like one side with specific information (name, address etc)

The other side to be bold, professional company name & logo. Striking.

Target Market(s)

B2B. Transport, mining, councils, environmentalist,

Industry/Entity Type

Petroleum

Contact Information for Business Card

Name; Peter Morrow
Position; Director
Email; pmorrow@korvanse.com.au
Address; PO Box 347, Kelmore, NSW, 2190
Website; www.korvanse.com.au

Colors

Designer to choose colors to be used in the design.

Requirements
Must have
• Clean, easy to read, professional & strong theme
Should not have
• too many colours, busy layout,

```html
<!DOCTYPE html>
<html lang="en">
<head>
<meta charset="utf-8">
<title>Korvan Advanced Energy – Business Card</title>
<link href="https://fonts.googleapis.com/css2?family=Poppins:wght@300;400;500&display=swap" rel="stylesheet">
<style>
  :root{
    --bg:#e4e2de;
    --card:#1b1d1f;
    --blue:#2f5f8e;
    --orange:#f26a1b;
    --text:#dcdcdc;
    --rule:#6a6d70;
    --silver:#b9b9b9;
  }
  *{box-sizing:border-box;margin:0;padding:0}
  html,body{width:1200px;height:1040px;overflow:hidden;background:var(--bg);font-family:'Poppins',sans-serif}
  .canvas{width:1200px;height:1040px;display:flex;flex-direction:column;align-items:center;justify-content:center;gap:30px}
  .card{position:relative;width:840px;height:475px;background:var(--card);border-radius:26px;
    box-shadow:0 4px 0 var(--orange),0 14px 24px rgba(0,0,0,.25);overflow:hidden;color:var(--text)}

  /* front */
  .brand{position:absolute;left:190px;top:70px;display:flex;align-items:center;gap:16px}
  .brand-dot{width:60px;height:60px;border-radius:50%;background:var(--orange);flex:none}
  .brand-name{font-weight:500;font-size:28px;color:var(--blue);letter-spacing:.5px;white-space:nowrap}

  .person{position:absolute;left:70px;top:262px}
  .person-name{font-size:30px;font-weight:400;color:var(--blue);line-height:1.1;white-space:nowrap}
  .person-role{font-size:17px;font-weight:400;color:var(--orange);margin-top:2px}

  .address{position:absolute;right:80px;top:270px;text-align:right;font-size:16px;line-height:1.45;font-weight:300;white-space:nowrap}

  .rule{position:absolute;left:70px;right:40px;top:338px;height:1px;background:var(--rule)}

  .contacts{position:absolute;left:70px;top:356px;list-style:none;font-size:17px;line-height:1.6;font-weight:300}
  .contacts li{display:flex;align-items:center;gap:12px;white-space:nowrap}
  .contacts svg{width:15px;height:15px;flex:none}

  /* back */
  .back-web{position:absolute;left:86px;top:50%;transform:translate(-50%,-50%) rotate(90deg);
    font-size:15px;letter-spacing:5px;font-weight:300;color:var(--text);white-space:nowrap}
  .back-mark{position:absolute;left:54%;top:50%;transform:translate(-50%,-50%);display:flex;flex-direction:column;align-items:center;gap:22px}
  .back-disc{width:190px;height:190px;border-radius:50%;background:linear-gradient(135deg,#d2d2d2,#8d8d8d)}
  .back-name{font-size:22px;font-weight:400;color:var(--silver);letter-spacing:2px;white-space:nowrap}
</style>
</head>
<body>
<main class="canvas">
  <section class="card card-front">
    <div class="brand">
      <span class="brand-dot"></span>
      <span class="brand-name">Korvan Advanced Energy</span>
    </div>
    <div class="person">
      <p class="person-name">Peter Morrow</p>
      <p class="person-role">Director</p>
    </div>
    <p class="address">PO Box 347<br>Kelmore, NSW, 2190</p>
    <div class="rule"></div>
    <ul class="contacts">
      <li><svg viewBox="0 0 16 16"><path fill="#2f5f8e" d="M4 1l3 3-2 2c1 2 3 4 5 5l2-2 3 3-2 3C7 15 1 9 1 3z"/></svg>369-555-0142</li>
      <li><svg viewBox="0 0 16 16"><rect x="1" y="3" width="14" height="10" rx="1" fill="#2f5f8e"/><path d="M1 4l7 5 7-5" stroke="#1b1d1f" stroke-width="1.4" fill="none"/></svg>pmorrow@korvanse.com.au</li>
      <li><svg viewBox="0 0 16 16"><circle cx="8" cy="8" r="7" fill="#2f5f8e"/><path d="M1 8h14M8 1c-3 4-3 10 0 14M8 1c3 4 3 10 0 14" stroke="#1b1d1f" stroke-width="1.2" fill="none"/></svg>www.korvanse.com.au</li>
    </ul>
  </section>
  <section class="card card-back">
    <p class="back-web">WWW.KORVANSE.COM.AU</p>
    <div class="back-mark">
      <span class="back-disc"></span>
      <span class="back-name">Korvan Advanced Energy</span>
    </div>
  </section>
</main>
</body>
</html>
```